Fieldgearhub.com

I need a catchy website, I will be selling multiples of tractor parts which will be looked up by the customer by manufacturer and model.
I do not have a logo for this yet so will need one also.

Target Market(s)

farmers, tractor drivers, contractors, tractor sales company, tractor parts company

Logo Text

Field Gear Hub

Font styles to use
Sans Serif

Requirements
Must have
• A function to search for parts through different headings
Must be easy to navigate and make it easy to find items they want.

```html
<!DOCTYPE html>
<html lang="en">
<head>
<meta charset="utf-8">
<title>Field Gear Hub – Tractor Parts</title>
<link href="https://fonts.googleapis.com/css2?family=Poppins:wght@300;400;500;600;700;800&display=swap" rel="stylesheet">
<style>
:root{
  --green:#2d6a2f;
  --ink:#2b2b2b;
  --text:#555;
  --muted:#8a8a8a;
  --line:#e4e4e4;
  --mint:#e6efeb;
  --tile:#ececec;
  --ghost:#f1f1f1;
  --white:#fff;
}
*{box-sizing:border-box;margin:0;padding:0}
html,body{width:1200px;height:3841px;overflow:hidden;background:var(--white)}
body{font-family:'Poppins',sans-serif;color:var(--ink);position:relative}

/* header */
.site-header{position:absolute;left:0;top:0;width:1200px;height:127px}
.brand{position:absolute;left:61px;top:34px;width:206px}
.brand-name{font-size:27px;font-weight:500;letter-spacing:-.2px;line-height:1.1;color:var(--ink)}
.brand-tag{font-size:12px;color:var(--text);margin-top:3px;padding-left:2px}
.search{position:absolute;left:370px;top:43px;width:451px;height:36px;border:1px solid var(--line);border-radius:18px;display:flex;align-items:center;padding:0 18px;font-size:11px;color:#999;justify-content:space-between}
.header-icons{position:absolute;top:46px;left:890px}
.header-icons svg{display:block}
.cart-count{position:absolute;left:73px;top:-2px;width:13px;height:13px;border-radius:50%;background:#111;color:#fff;font-size:8px;text-align:center;line-height:13px}
.currency{position:absolute;left:1010px;top:47px;display:flex;align-items:center;gap:6px;font-size:11px;font-weight:600}
.flag{width:24px;height:24px;border-radius:50%;background:linear-gradient(135deg,#2b3f8f,#c83a3a)}

/* hero */
.hero{position:absolute;left:0;top:127px;width:1200px;height:575px;background:var(--mint);overflow:hidden}
.hero-ghost{position:absolute;left:30px;top:113px;font-size:118px;font-weight:800;color:rgba(0,0,0,.06);line-height:1;letter-spacing:2px}
.hero-ghost2{position:absolute;left:34px;top:255px;font-size:100px;font-weight:300;color:rgba(0,0,0,.06);line-height:1;letter-spacing:4px}
.hero-title{position:absolute;left:121px;top:202px;font-size:54px;line-height:1;color:var(--ink);z-index:2}
.hero-title b{font-weight:800}
.hero-title span{font-weight:300}
.hero-copy{position:absolute;left:121px;top:280px;width:320px;font-size:12.5px;line-height:21px;color:var(--text)}
.btn-outline{position:absolute;display:flex;align-items:center;justify-content:center;border:1.5px solid #444;border-radius:24px;font-size:11px;font-weight:600;color:var(--ink);letter-spacing:.3px}
.hero-photo{position:absolute;left:514px;top:37px;width:596px;height:469px;border-radius:40px;background:radial-gradient(ellipse at 55% 45%,#4b8f3c 0%,#3a5a34 35%,#3b3b3b 65%,rgba(230,239,235,0) 78%)}
.dots{position:absolute;left:580px;top:536px;display:flex;gap:8px}
.dots i{width:9px;height:9px;border-radius:50%;background:#bfc7c4;display:block}
.dots i:first-child{background:#333}

/* about */
.about-frame{position:absolute;left:83px;top:820px;width:416px;height:444px;border:4px solid var(--green)}
.about-gap{position:absolute;left:490px;top:891px;width:20px;height:316px;background:var(--white)}
.about-photo{position:absolute;left:164px;top:872px;width:253px;height:332px;border-radius:30px;background:radial-gradient(ellipse at center,#c9c9c9 0%,#9a9a9a 55%,#fff 75%)}
.about-title{position:absolute;left:463px;top:928px;font-size:30px;font-weight:800}
.about-body{position:absolute;left:464px;top:985px;width:510px;font-size:12.5px;line-height:21px;color:var(--text)}
.about-body p{margin-bottom:20px}
.link-more{position:absolute;font-size:11.5px;font-weight:600;letter-spacing:.2px}
.about-ghost{position:absolute;left:1034px;top:760px;writing-mode:vertical-rl;font-size:156px;font-weight:800;color:var(--ghost);line-height:112px;letter-spacing:-2px}

/* products */
.section-title{position:absolute;width:1200px;left:0;text-align:center;font-weight:800;font-size:32px}
.tabs{position:absolute;top:1447px;left:0;width:1200px;display:flex;justify-content:center;gap:40px;font-size:12px;color:var(--text)}
.tabs .active{color:var(--ink);font-weight:500}
.card{position:absolute;width:231px}
.card-media{height:245px;background:var(--tile);position:relative}
.card-media .shape{position:absolute;left:50%;top:50%;transform:translate(-50%,-50%);width:150px;height:130px;border-radius:50%}
.badge{position:absolute;right:0;top:0;background:var(--green);color:#fff;font-size:11px;font-weight:500;padding:2px 8px}
.card-info{display:flex;align-items:center;height:40px;font-size:12px}
.card-info .name{color:var(--ink);width:98px}
.card-info .price{color:var(--muted);padding-left:12px;border-left:1px solid var(--line);width:80px}
.card-info .cart{margin-left:auto;padding-left:14px;border-left:1px solid var(--line);margin-right:22px;display:flex}
.card.hover{background:#f7f7f7;height:337px}
.card.hover .card-info{padding-left:12px}
.card.hover .card-info .name{width:110px}
.card.hover .card-info .price{width:70px}
.card-desc{padding:0 12px;font-size:10.5px;line-height:13px;color:var(--text)}
.quick-tools{position:absolute;right:0;top:0;width:37px;height:118px;background:#fff;display:flex;flex-direction:column;align-items:center;justify-content:space-around}

/* testimonials */
.reviews-ghost{position:absolute;left:0;width:1200px;text-align:center;top:2288px;font-size:156px;font-weight:800;color:var(--ghost);letter-spacing:4px;line-height:1}
.quote{position:absolute;top:2500px;width:472px;height:247px;border:3px solid var(--green);text-align:center}
.quote-gap{position:absolute;top:-4px;left:186px;width:100px;height:6px;background:var(--white)}
.avatar{position:absolute;top:-28px;left:209px;width:54px;height:54px;border-radius:50%;background:linear-gradient(#c8c3bb,#8c8479)}
.quote p{margin:56px 48px 0;font-size:13.5px;line-height:26px;color:var(--text)}
.quote .who{margin-top:20px;font-size:12px;color:var(--text)}
.quote .who b{font-weight:500;color:var(--ink)}
.nav-arrows{position:absolute;top:2781px;left:567px;display:flex;gap:10px}
.nav-arrows span{width:27px;height:27px;border-radius:50%;border:1px solid var(--line);display:flex;align-items:center;justify-content:center;font-size:13px}

/* drivers */
.drivers{position:absolute;left:0;top:2882px;width:1200px;height:384px;background:linear-gradient(90deg,#dbe7e2 40%,#eef3ea 100%)}
.drivers-photo{position:absolute;left:0;top:0;width:611px;height:384px;background:linear-gradient(110deg,#2f3640 0%,#4a5464 40%,#a79bb0 70%,rgba(219,231,226,0) 100%)}
.drivers-title{position:absolute;right:114px;top:110px;font-size:54px;line-height:1}
.drivers-title b{font-weight:800}
.drivers-title span{font-weight:300}
.drivers-copy{position:absolute;right:114px;top:183px;width:320px;text-align:right;font-size:12.5px;line-height:21px;color:var(--text)}

/* footer */
.footer-brand{left:61px;top:3371px}
.footer-about{position:absolute;left:64px;top:3452px;width:320px;font-size:12.3px;line-height:20.5px;color:var(--text)}
.footer-col{position:absolute;top:3372px}
.footer-col h4{font-size:13.5px;font-weight:500;color:var(--ink);margin-bottom:29px}
.footer-col li{list-style:none;font-size:12px;color:var(--text);line-height:31px}
.socials{position:absolute;left:822px;top:3434px;display:flex;gap:14px;font-size:12px;color:var(--ink)}
.newsletter-title{position:absolute;left:822px;top:3497px;font-size:13.5px;font-weight:500}
.newsletter-sub{position:absolute;left:822px;top:3526px;font-size:12px;color:var(--text)}
.newsletter{position:absolute;left:818px;top:3568px;width:315px;height:38px;border:1px solid var(--line);border-radius:19px;display:flex;align-items:center;justify-content:space-between;padding:0 18px;font-size:11.5px;color:#9a9a9a}
.newsletter b{color:var(--ink);font-weight:400}
.payments{position:absolute;left:822px;top:3645px;display:flex;gap:20px;font-size:13px;font-weight:600;color:var(--ink)}
.footer-rule{position:absolute;left:0;top:3747px;width:1200px;height:1px;background:var(--line)}
.copyright{position:absolute;left:0;top:3781px;width:1200px;text-align:center;font-size:11.5px;color:var(--muted)}
.copyright b{color:var(--ink);font-weight:500}
</style>
</head>
<body>

<header class="site-header">
  <div class="brand">
    <div class="brand-name">field gear hub</div>
    <div class="brand-tag">tractor spares online</div>
  </div>
  <div class="search">
    <span>OEM Part No. / Model / Keyword</span>
    <svg width="20" height="20" viewBox="0 0 20 20" fill="none" stroke="#222" stroke-width="1.6"><circle cx="8.5" cy="8.5" r="6.5"/><path d="M13.5 13.5L18 18"/></svg>
  </div>
  <div class="header-icons">
    <svg style="position:absolute;left:4px;top:0" width="22" height="24" viewBox="0 0 22 24" fill="none" stroke="#222" stroke-width="1.5"><circle cx="11" cy="7" r="5"/><path d="M2 23c0-5 4-8 9-8s9 3 9 8z"/></svg>
    <svg style="position:absolute;left:56px;top:1px" width="24" height="22" viewBox="0 0 24 22" fill="none" stroke="#222" stroke-width="1.5"><path d="M1 2h4l3 12h12l2-9H6"/><circle cx="10" cy="19" r="1.6"/><circle cx="18" cy="19" r="1.6"/></svg>
    <span class="cart-count">0</span>
  </div>
  <div class="currency"><span class="flag"></span>GBP <span style="font-size:8px">⌄</span></div>
  <svg style="position:absolute;left:1108px;top:54px" width="17" height="13" viewBox="0 0 17 13" stroke="#222" stroke-width="1.8"><path d="M0 1h17M0 6.5h17M0 12h17"/></svg>
</header>

<section class="hero">
  <div class="hero-ghost">TRACTOR</div>
  <div class="hero-ghost2">PARTS</div>
  <div class="hero-photo" role="img" aria-label="Green modern tractor with large black tyres"></div>
  <h1 class="hero-title"><b>TRACTOR</b> <span>PARTS</span></h1>
  <p class="hero-copy">farmers, tractor drivers, contractors, tractor sales company, tractor parts company</p>
  <a class="btn-outline" style="left:123px;top:360px;width:163px;height:44px">LEARN MORE</a>
  <div class="dots"><i></i><i></i><i></i></div>
</section>

<section class="about">
  <div class="about-ghost">ABOUT</div>
  <div class="about-frame"></div>
  <div class="about-gap"></div>
  <div class="about-photo" role="img" aria-label="Silver hydraulic pump with gear"></div>
  <h2 class="about-title">ABOUT US</h2>
  <div class="about-body">
    <p>Donec accumsan auctor iaculis. Sed suscipit arcu ligula, at egestas magna molestie a. Proin ac ex maximus ultrices justo eget, sodales orci. Faucibus ac laoreet sed.</p>
    <p>Aliquam egestas libero ac turpis pharetra, in vehicula lacus scelerisque. Vestibulum ut sem laoreet, feugiat tellus at, hendrerit arcu.</p>
  </div>
  <a class="link-more" style="left:464px;top:1151px">LEARN MORE</a>
</section>

<section class="products">
  <h2 class="section-title" style="top:1388px">OUR PRODUCTS</h2>
  <nav class="tabs">
    <span class="active">Ridgeway Agri-Belts</span><span>Baler Parts</span><span>Conbine Parts</span><span>Hydraulic Pumps</span>
  </nav>

  <div class="card" style="left:92px;top:1533px">
    <div class="card-media"><div class="shape" role="img" aria-label="Green round baler" style="background:radial-gradient(#3b9b3a,#2c7a2c 60%,transparent 70%)"></div><span class="badge">New</span></div>
    <div class="card-info"><span class="name">Cotton T-Shirt</span><span class="price">$35.00</span><span class="cart"><svg width="16" height="15" viewBox="0 0 24 22" fill="none" stroke="#222" stroke-width="1.8"><path d="M1 2h4l3 12h12l2-9H6"/><circle cx="10" cy="19" r="1.6"/><circle cx="18" cy="19" r="1.6"/></svg></span></div>
  </div>
  <div class="card hover" style="left:353px;top:1533px">
    <div class="card-media"><div class="shape" role="img" aria-label="Red and grey gear pump" style="background:radial-gradient(#9b4a44,#6a625a 60%,transparent 70%)"></div>
      <div class="quick-tools">
        <svg width="18" height="16" viewBox="0 0 24 22" fill="none" stroke="#222" stroke-width="1.6"><path d="M1 2h4l3 12h12l2-9H6"/><circle cx="10" cy="19" r="1.6"/><circle cx="18" cy="19" r="1.6"/></svg>
        <svg width="16" height="18" viewBox="0 0 22 24" fill="none" stroke="#222" stroke-width="1.6"><circle cx="11" cy="7" r="5"/><path d="M2 23c0-5 4-8 9-8s9 3 9 8z"/></svg>
        <svg width="17" height="17" viewBox="0 0 20 20" fill="none" stroke="#222" stroke-width="1.6"><circle cx="8.5" cy="8.5" r="6.5"/><path d="M13.5 13.5L18 18"/></svg>
      </div>
    </div>
    <div class="card-info"><span class="name">Cotton T-Shirt</span><span class="price">$35.00</span><span class="cart"><svg width="16" height="15" viewBox="0 0 24 22" fill="none" stroke="#222" stroke-width="1.8"><path d="M1 2h4l3 12h12l2-9H6"/><circle cx="10" cy="19" r="1.6"/><circle cx="18" cy="19" r="1.6"/></svg></span></div>
    <p class="card-desc">Donec accumsan auctor iaculis. Sed suscipit arcu ligula, at egestas</p>
  </div>
  <div class="card" style="left:612px;top:1533px">
    <div class="card-media"><div class="shape" role="img" aria-label="Blue ribbed drive belt" style="background:radial-gradient(#6f88b8,#38558e 60%,transparent 70%)"></div><span class="badge">New</span></div>
    <div class="card-info"><span class="name">Cotton T-Shirt</span><span class="price">$35.00</span><span class="cart"><svg width="16" height="15" viewBox="0 0 24 22" fill="none" stroke="#222" stroke-width="1.8"><path d="M1 2h4l3 12h12l2-9H6"/><circle cx="10" cy="19" r="1.6"/><circle cx="18" cy="19" r="1.6"/></svg></span></div>
  </div>
  <div class="card" style="left:873px;top:1533px">
    <div class="card-media"><div class="shape" role="img" aria-label="Coiled black V-belt" style="background:radial-gradient(#555,#1e1e1e 60%,transparent 70%)"></div></div>
    <div class="card-info"><span class="name">Cotton T-Shirt</span><span class="price">$35.00</span><span class="cart"><svg width="16" height="15" viewBox="0 0 24 22" fill="none" stroke="#222" stroke-width="1.8"><path d="M1 2h4l3 12h12l2-9H6"/><circle cx="10" cy="19" r="1.6"/><circle cx="18" cy="19" r="1.6"/></svg></span></div>
  </div>

  <div class="card" style="left:92px;top:1903px">
    <div class="card-media"><div class="shape" role="img" aria-label="Wooden baler block" style="background:radial-gradient(#e8a54a,#c98530 60%,transparent 70%)"></div></div>
    <div class="card-info"><span class="name">Cotton T-Shirt</span><span class="price">$35.00</span><span class="cart"><svg width="16" height="15" viewBox="0 0 24 22" fill="none" stroke="#222" stroke-width="1.8"><path d="M1 2h4l3 12h12l2-9H6"/><circle cx="10" cy="19" r="1.6"/><circle cx="18" cy="19" r="1.6"/></svg></span></div>
  </div>
  <div class="card" style="left:353px;top:1903px">
    <div class="card-media"><div class="shape" role="img" aria-label="Silver hydraulic gear pump" style="background:radial-gradient(#cfcfcf,#555 60%,transparent 70%)"></div><span class="badge">New</span></div>
    <div class="card-info"><span class="name">Cotton T-Shirt</span><span class="price">$35.00</span><span class="cart"><svg width="16" height="15" viewBox="0 0 24 22" fill="none" stroke="#222" stroke-width="1.8"><path d="M1 2h4l3 12h12l2-9H6"/><circle cx="10" cy="19" r="1.6"/><circle cx="18" cy="19" r="1.6"/></svg></span></div>
  </div>
  <div class="card" style="left:612px;top:1903px">
    <div class="card-media"><div class="shape" role="img" aria-label="Green hydraulic pump" style="background:radial-gradient(#45b06a,#23774a 60%,transparent 70%)"></div></div>
    <div class="card-info"><span class="name">Cotton T-Shirt</span><span class="price">$35.00</span><span class="cart"><svg width="16" height="15" viewBox="0 0 24 22" fill="none" stroke="#222" stroke-width="1.8"><path d="M1 2h4l3 12h12l2-9H6"/><circle cx="10" cy="19" r="1.6"/><circle cx="18" cy="19" r="1.6"/></svg></span></div>
  </div>
  <div class="card" style="left:873px;top:1903px">
    <div class="card-media"><div class="shape" role="img" aria-label="Red cylinder with chrome rod end" style="background:radial-gradient(#c24a3b,#8a8f96 60%,transparent 70%)"></div><span class="badge">New</span></div>
    <div class="card-info"><span class="name">Cotton T-Shirt</span><span class="price">$35.00</span><span class="cart"><svg width="16" height="15" viewBox="0 0 24 22" fill="none" stroke="#222" stroke-width="1.8"><path d="M1 2h4l3 12h12l2-9H6"/><circle cx="10" cy="19" r="1.6"/><circle cx="18" cy="19" r="1.6"/></svg></span></div>
  </div>
</section>

<section class="testimonials">
  <div class="reviews-ghost">REVIEWS</div>
  <h2 class="section-title" style="top:2344px">TESTIMONIALS</h2>
  <div class="quote" style="left:106px">
    <span class="quote-gap"></span>
    <div class="avatar" role="img" aria-label="Customer portrait"></div>
    <p>" Donec accumsan auctor iaculis. Sed suscipit arcu ligula, at egestas magna molestie a. Proin ac ex maximus ultrices justo eget, sodales orci. Faucibus ac laoreet sed. Aliquam egestas libero ac turpis</p>
    <div class="who"><b>Tessa Morland</b> &nbsp;-&nbsp; Riverton, Ohio</div>
  </div>
  <div class="quote" style="left:618px">
    <span class="quote-gap"></span>
    <div class="avatar" role="img" aria-label="Customer portrait"></div>
    <p>" Donec accumsan auctor iaculis. Sed suscipit arcu ligula, at egestas magna molestie a. Proin ac ex maximus ultrices justo eget, sodales orci. Faucibus ac laoreet sed. Aliquam egestas libero ac turpis</p>
    <div class="who"><b>Tessa Morland</b> &nbsp;-&nbsp; Riverton, Ohio</div>
  </div>
  <div class="nav-arrows"><span>←</span><span>→</span></div>
</section>

<section class="drivers">
  <div class="drivers-photo" role="img" aria-label="Tractor driver standing beside a tractor cab"></div>
  <h2 class="drivers-title"><b>TRACTOR</b> <span>DRIVERS</span></h2>
  <p class="drivers-copy">farmers, tractor drivers, contractors, tractor sales company, tractor parts company</p>
  <a class="btn-outline" style="left:925px;top:264px;width:161px;height:43px">LEARN MORE</a>
</section>

<footer class="site-footer">
  <div class="brand footer-brand">
    <div class="brand-name">field gear hub</div>
    <div class="brand-tag">tractor spares online</div>
  </div>
  <p class="footer-about">Field Gear Hub Limited trading as fieldgearhub.com is registered in England and Wales, Company Number 08217634, our VAT registration is 314907552. Parts supplied by Field Gear Hub Limited are not manufactured by the original equipment manufacturer. Original manufacturer's name, part numbers and descriptions are quoted for reference purposes only and are not intended to indicate or suggest that our replacement parts are made by the original equipment manufacturer.</p>
  <div class="footer-col" style="left:441px">
    <h4>Useful Links</h4>
    <ul><li>Search</li><li>About Us</li><li>Contact Us</li><li>Payment Info</li><li>Delivery</li><li>Return and Refund Policy</li><li>Privacy Policy</li><li>Terms &amp; Conditions</li></ul>
  </div>
  <div class="footer-col" style="left:633px">
    <h4>Catalogues</h4>
    <ul><li>Strongline Agri-Belts</li><li>Ridgeway Agri-Belts</li></ul>
  </div>
  <div class="footer-col" style="left:822px"><h4>Follow Us</h4></div>
  <div class="socials"><span>Barnly</span><span>Chirrup</span><span>Fieldgram</span><span>Pinrow</span></div>
  <div class="newsletter-title">Be in the know</div>
  <div class="newsletter-sub">Sign up for the latest news, offers and styles</div>
  <div class="newsletter"><span>Your Mail Address</span><b>→</b></div>
  <div class="payments"><span>Cardmere</span><span>Vantra</span><span>Quillpay</span><span>Tillway</span></div>
  <div class="footer-rule"></div>
  <p class="copyright">© 2020, <b>fieldgearhub.com</b>. All Rights Reserved.</p>
</footer>

</body>
</html>
```